Simon & Lorna's Yuletide Unwind Bash

Invitation to a party 60-80 people at a private residence. Age range 30-40s.

Themes: summer/casual/Australian backyard/local community

**For delivery via both email and printed copy**
Would like one document suitable for both purposes or two versions for electronic or paper invitation. I will arrange printing so please prepare it in a suitable format.

Specimen text attached. Address and phone contact to follow by message with successful bidder

Thanks!
Simon

Target Market(s)

Locals, friends. Party attendees will typicaly be parents in their forties who who be leaving the kids at home for a relaxed party night, and walking home afterward

Industry/Entity Type

Community

Font styles to use
Sans Serif

Requirements
Should not have
• Cliche Australiana imagery. No kangaroos etc

```html
<!DOCTYPE html>
<html lang="en">
<head>
<meta charset="utf-8">
<title>Simon &amp; Lorna's Yuletide Unwind Bash</title>
<link rel="stylesheet" href="https://fonts.googleapis.com/css2?family=Poiret+One&display=swap">
<style>
  :root {
    --bg-charcoal: #2a2928;
    --bg-slate: #343331;
    --glow-amber: #6b4c38;
    --glow-umber: #3f332c;
    --text-cream: #eeece6;
    --text-soft: #d8d4cc;
  }
  * { margin: 0; padding: 0; box-sizing: border-box; }
  html, body {
    width: 800px;
    height: 1200px;
    overflow: hidden;
    background: var(--bg-charcoal);
  }
  .invitation {
    position: relative;
    width: 800px;
    height: 1200px;
    overflow: hidden;
    background:
      radial-gradient(ellipse at 30% 75%, var(--bg-slate) 0%, transparent 60%),
      radial-gradient(ellipse at 80% 95%, #302f2d 0%, transparent 55%),
      var(--bg-charcoal);
    font-family: "Poiret One", sans-serif;
    color: var(--text-cream);
    text-align: center;
  }
  .fairy-lights-photo {
    position: absolute;
    left: 0;
    top: 0;
    width: 800px;
    height: 600px;
    display: block;
  }
  .intro {
    position: absolute;
    top: 424px;
    left: 0;
    width: 800px;
    font-size: 24px;
    line-height: 48px;
    letter-spacing: 1.5px;
    color: var(--text-soft);
  }
  .title {
    position: absolute;
    top: 584px;
    left: 0;
    width: 800px;
    font-weight: 400;
    font-size: 54px;
    line-height: 96px;
    letter-spacing: 2px;
  }
  .guest-note {
    position: absolute;
    top: 856px;
    left: 0;
    width: 800px;
    font-size: 29px;
    letter-spacing: 1.5px;
  }
  .details {
    position: absolute;
    top: 968px;
    left: 0;
    width: 800px;
    font-size: 27px;
    line-height: 50px;
    letter-spacing: 1.5px;
    font-style: normal;
  }
</style>
</head>
<body>
  <main class="invitation">
    <svg class="fairy-lights-photo" viewBox="0 0 800 600" role="img" aria-label="Photograph of warm fairy lights strung in soft focus against a textured wall" preserveAspectRatio="none">
      <defs>
        <linearGradient id="photo-tone" x1="0" y1="0" x2="0" y2="1">
          <stop offset="0" stop-color="var(--glow-umber)"/>
          <stop offset="0.35" stop-color="var(--glow-amber)" stop-opacity="0.85"/>
          <stop offset="0.7" stop-color="var(--glow-umber)" stop-opacity="0.6"/>
          <stop offset="1" stop-color="var(--bg-charcoal)" stop-opacity="0"/>
        </linearGradient>
      </defs>
      <rect width="800" height="600" fill="url(#photo-tone)"/>
    </svg>

    <p class="intro">Leave the kids at home<br>and let your hair down at</p>

    <h1 class="title">Simon &amp; Lorna's<br>Yuletide Unwind Bash</h1>

    <p class="guest-note">- For Hollowmere Heights and friends -</p>

    <address class="details">
      Saturday 2 January<br>
      From 6pm `til late<br>
      14 Lantern Lane,<br>
      Hollowmere Heights
    </address>
  </main>
</body>
</html>
```